Marketing folder with booklet and brochure. Slot for business card

We are a dual-branded commercial and residential flooring installation company. Carpet, resilient, wood, tile, flooring repairs, sand and finish wood. We like designs using red, white, and blue. Custom Font style is Luna Bar, available upon request Content available on our website qendwick-surfaces.net. Ideally would like a small booklet of services, letterhead for intro letter, folder, and possibly tri-fold.

Target Market(s)

Builders, designers, and contractors. We do not typically work for the general public

Industry/Entity Type

Construction

Contact Information for Business Card

We currently have business cards, but because we want a card slot in the folder, we might have to match toward our print package. Check out our web site qendwick-surfaces.net

Font styles to use
Serif

Colors
0456a4
ec1f27
ffffff

```html
<!DOCTYPE html>
<html lang="en">
<head>
<meta charset="utf-8">
<title>Qendwick Surfaces – Marketing Folder</title>
<link href="https://fonts.googleapis.com/css2?family=Oswald:wght@300;400;500&family=Open+Sans:wght@400;600;700&family=Kalam:wght@400&display=swap" rel="stylesheet">
<style>
  :root{
    --blue:#0456a4;
    --red:#ec1f27;
    --white:#ffffff;
    --stage:#9b9b9b;
    --ink:#2a2a2a;
  }
  *{box-sizing:border-box;margin:0;padding:0}
  html,body{width:1200px;height:1200px;overflow:hidden;background:var(--stage)}
  .canvas{position:relative;width:1200px;height:1200px;background:var(--stage)}
  .page{position:absolute;width:360px;height:520px;overflow:hidden;box-shadow:0 6px 18px rgba(0,0,0,.28)}
  .page svg{position:absolute;inset:0}

  /* Folder cover */
  .cover{left:220px;top:50px;background:var(--white)}
  .cover-photo{position:absolute;left:0;top:0;width:360px;height:300px;
    background:linear-gradient(135deg,#242426 0%,#37332f 38%,#5e412c 60%,#8c6a4b 78%,#b99b78 100%)}
  .cover-swatches{position:absolute;left:0;top:300px;width:70px;height:220px;
    background:linear-gradient(180deg,#cfc9bf 0%,#e8e4dd 35%,#cdbba2 70%,#a98f72 100%)}
  .brand{position:absolute;font-family:'Oswald',sans-serif;font-weight:400;color:var(--white);letter-spacing:.5px;white-space:nowrap}
  .cover .brand{left:120px;top:58px;font-size:30px;line-height:1.05;text-transform:uppercase}
  .brand .dot{display:inline-block;width:10px;height:10px;background:var(--red);margin-right:8px;vertical-align:middle}
  .cover-strap{position:absolute;left:22px;top:150px;width:316px;font-family:'Oswald',sans-serif;font-weight:400;font-size:17px;color:var(--white);text-align:center}
  .tagline{position:absolute;text-align:center}
  .tagline .name{font-family:'Kalam',cursive;font-size:26px;color:var(--blue);line-height:1;white-space:nowrap}
  .tagline .sub{font-family:'Open Sans',sans-serif;font-size:16px;color:var(--white);margin-top:6px}
  .cover .tagline{left:116px;top:414px;width:230px}

  /* Insert sheet */
  .sheet{left:620px;top:50px;background:var(--red)}
  .sheet-photo{position:absolute;left:0;top:0;width:360px;height:290px;
    background:linear-gradient(160deg,#f37a7e 0%,#ee4a50 55%,#ec2f36 100%)}
  .contact{position:absolute;left:28px;top:306px;font-family:'Open Sans',sans-serif;color:var(--white);font-size:10.5px;line-height:1.4}
  .contact h3{font-size:10.5px;font-weight:700;text-transform:uppercase;letter-spacing:.4px;margin-top:8px}
  .contact h3:first-child{margin-top:0}
  .sheet .brand{right:24px;bottom:16px;font-size:19px;line-height:1;text-transform:uppercase;text-align:right}

  /* Inside spread */
  .inside-left{left:240px;top:620px;box-shadow:none;background:transparent}
  .inside-right{left:600px;top:620px;background:var(--white)}
  .services-title{position:absolute;left:0;top:34px;width:360px;text-align:center;font-family:'Oswald',sans-serif;font-weight:400;font-size:22px;letter-spacing:12px;color:var(--blue)}
  .services{position:absolute;top:84px;font-family:'Open Sans',sans-serif}
  .services.col-a{left:34px}
  .services.col-b{left:196px}
  .services h4{font-size:10px;font-weight:700;color:var(--red);text-transform:uppercase;margin-top:10px}
  .services h4:first-child{margin-top:0}
  .services ul{list-style:none}
  .services li{font-size:10px;color:var(--blue);line-height:1.45;padding-left:9px;position:relative}
  .services li::before{content:"";position:absolute;left:0;top:6px;width:3px;height:3px;background:var(--blue);border-radius:50%}
  .inside-right .tagline{left:10px;top:418px;width:210px}
</style>
</head>
<body>
<main class="canvas">

  <!-- Folder outside front -->
  <section class="page cover">
    <div class="cover-photo" role="img" aria-label="Fan of wood-look flooring plank samples over a dark wood background"></div>
    <div class="cover-swatches" role="img" aria-label="Light wood-look flooring samples fanning down the left edge"></div>
    <svg width="360" height="520" viewBox="0 0 360 520">
      <defs>
        <clipPath id="coverPocket"><path d="M70 520 L70 430 Q78 308 200 300 L360 300 L360 520 Z"/></clipPath>
      </defs>
      <path d="M70 520 L70 430 Q78 308 200 300 L360 300 L360 520 Z" fill="var(--white)"/>
      <path d="M70 520 L70 430 Q78 308 200 300" fill="none" stroke="rgba(0,0,0,.18)" stroke-width="3"/>
      <circle cx="245" cy="440" r="150" fill="var(--red)"/>
      <circle cx="245" cy="440" r="150" fill="var(--red)" clip-path="url(#coverPocket)"/>
    </svg>
    <div class="brand"><span class="dot"></span>Qendwick<br>Surfaces</div>
    <p class="cover-strap">Twin Cities' Premier Flooring Installation Company!</p>
    <div class="tagline">
      <div class="name">Beyond The Grain</div>
      <div class="sub">Floors and More</div>
    </div>
  </section>

  <!-- Insert sheet -->
  <section class="page sheet">
    <div class="sheet-photo" role="img" aria-label="Red-tinted photo of a commercial conference room with installed flooring"></div>
    <div class="contact">
      <h3>Showroom Address</h3>
      <p>2270 Larkspur St NE #140,<br>Northvale, MN 55490<br>555 014 2871<br>Monday – Friday 8AM – 4PM</p>
      <h3>Warehouse Address</h3>
      <p>3915 Ashgrove Ave N,<br>Pinecrest, MN 55498<br>555 014 6630<br>Monday – Friday 8AM – 4PM</p>
    </div>
    <div class="brand"><span class="dot"></span>Qendwick Surfaces</div>
  </section>

  <!-- Inside left flap: services -->
  <section class="page inside-left">
    <svg width="360" height="520" viewBox="0 0 360 520">
      <path d="M0 0 L360 0 L360 520 L150 520 Q150 370 0 360 Z" fill="var(--white)"/>
      <path d="M150 520 Q150 370 0 360" fill="none" stroke="rgba(0,0,0,.12)" stroke-width="2"/>
    </svg>
    <h2 class="services-title">SERVICES</h2>
    <div class="services col-a">
      <h4>Carpet Installation</h4>
      <ul><li>Hallway</li><li>Conference room</li><li>Lobbies</li><li>Office</li></ul>
      <h4>Carpet Repair</h4>
      <ul><li>Burns, holes, and stains</li><li>Patches</li><li>Restretching</li><li>Seams</li><li>Seam failure</li></ul>
    </div>
    <div class="services col-b">
      <h4>Hardwood Installation</h4>
      <ul><li>Engineered</li><li>Prefinished</li><li>Laminate</li><li>Site finished</li></ul>
      <h4>Resilient Installation</h4>
      <ul><li>Sheet vinyl</li><li>Vinyl tile</li><li>Luxury vinyl</li></ul>
      <h4>Tile Installation</h4>
      <ul><li>Backsplashes</li><li>Floors</li><li>Bathrooms</li></ul>
    </div>
  </section>

  <!-- Inside right: pocket -->
  <section class="page inside-right">
    <svg width="360" height="520" viewBox="0 0 360 520">
      <rect x="0" y="330" width="360" height="190" fill="var(--white)"/>
      <line x1="0" y1="330" x2="360" y2="330" stroke="rgba(0,0,0,.15)" stroke-width="3"/>
      <circle cx="115" cy="520" r="190" fill="var(--red)"/>
    </svg>
    <div class="tagline">
      <div class="name">Beyond The Grain</div>
      <div class="sub">Floors and More</div>
    </div>
  </section>

</main>
</body>
</html>
```